KoviBelo

This involves designing the UI for an app used for training with others. The app will give the user a lists of sports they can create events on. The kovi belo logo design should be quite prominent in the app ui design. I have uploaded a sample. And also pictures of my attempt at designing this. I would like this design enhanced for android and ios. the sports being offered are as follows.

Running
Long Distance -
Middle distance -
Sprint -

Cycling
Spinning -
Mountain biking - just the same image places at an angle with a line underneath
Road - maybe with the road laid out below
Sprint - with lines to indicate speed maybe

Gym -
Weightlifting
Ironloop
Yoga -
Palates -

Combat -
Boxing
BJJ
Kickboxing
Wrestling

Water Sports -
Swimming -
Water polo -
Kayaking -

Games -
Basketball
Football
Golf -
Badmington -

Walking - -
Hiking -
City Walking -

Cover art.

Industry/Entity Type

Health And Wellness

Number of Pages Required

1 page

Requirements
Must have
• Android and iOS design

```html
<!DOCTYPE html>
<html lang="en">
<head>
<meta charset="utf-8">
<title>KoviBelo – User Profile</title>
<link rel="stylesheet" href="https://fonts.googleapis.com/css2?family=Exo+2:ital,wght@1,800&family=Open+Sans:wght@700&display=swap">
<style>
  :root {
    --black: #000000;
    --deep-blue: #0b3a75;
    --panel-blue: #0f4586;
    --band-blue: #0a2f62;
    --bar-light: #1d5ba3;
    --edge-blue: #2a6cb8;
    --accent: #2aa9e6;
    --icon-blue: #3ea8e4;
    --white: #ffffff;
    --track-dark: #061a33;
  }
  html, body {
    margin: 0;
    padding: 0;
    width: 675px;
    height: 1200px;
    overflow: hidden;
    background: var(--black);
  }
  .screen {
    position: relative;
    width: 675px;
    height: 1200px;
    overflow: hidden;
    background: var(--black);
    font-family: "Open Sans", Arial, sans-serif;
    color: var(--white);
  }
  .frame {
    position: absolute;
    inset: 0;
  }
  .section-title {
    position: absolute;
    left: 0;
    width: 675px;
    text-align: center;
    font-family: "Exo 2", "Arial Black", sans-serif;
    font-style: italic;
    font-weight: 800;
    letter-spacing: 2px;
    font-size: 36px;
    margin: 0;
    text-shadow: 0 2px 3px rgba(0,0,0,0.45);
  }
  .profile-title { top: 168px; }
  .preferences-title { top: 584px; }
  .avatar {
    position: absolute;
    left: 36px;
    top: 254px;
    width: 293px;
    height: 297px;
    box-sizing: border-box;
    border: 5px solid var(--track-dark);
    background: linear-gradient(160deg, #b58a64 0%, #6c4a33 45%, #8aa4c9 80%, #c9d4e6 100%);
  }
  .avatar-camera {
    position: absolute;
    left: 8px;
    bottom: 8px;
  }
  .profile-name, .profile-age {
    position: absolute;
    left: 421px;
    margin: 0;
    font-size: 28px;
    font-weight: 700;
  }
  .profile-name { top: 352px; }
  .profile-age { top: 422px; }
  .pref-label {
    position: absolute;
    left: 29px;
    top: 678px;
    margin: 0;
    font-size: 29px;
    font-weight: 700;
  }
  .distance-slider {
    position: absolute;
    left: 218px;
    top: 674px;
    width: 425px;
    height: 50px;
  }
  .slider-track {
    position: absolute;
    left: 0; right: 0;
    top: 23px;
    height: 5px;
    background: var(--track-dark);
    border-radius: 3px;
  }
  .slider-fill {
    position: absolute;
    left: 0;
    top: 22px;
    width: 203px;
    height: 6px;
    background: var(--accent);
    border-radius: 3px;
  }
  .slider-thumb {
    position: absolute;
    left: 178px;
    top: 0;
    width: 50px;
    height: 50px;
    border-radius: 50%;
    background: radial-gradient(circle at 38% 32%, #ffffff 0%, #d9dde2 45%, #8c949c 100%);
    box-shadow: 0 2px 4px rgba(0,0,0,0.5);
  }
  .nav-item {
    position: absolute;
  }
  .nav-profile { left: 50px; top: 1050px; }
  .nav-training { left: 262px; top: 1040px; }
  .nav-group { left: 545px; top: 1053px; }
</style>
</head>
<body>
<main class="screen">
  <svg class="frame" width="675" height="1200" viewBox="0 0 675 1200" aria-hidden="true">
    <!-- upper panel with centre tab -->
    <path d="M0 160 L0 138 L255 138 L278 112 L397 112 L420 138 L675 138 L675 160 Z" fill="var(--band-blue)"/>
    <path d="M278 112 L397 112 L420 138 L255 138 Z" fill="var(--panel-blue)" stroke="var(--edge-blue)" stroke-width="2"/>
    <!-- profile title bar -->
    <rect x="0" y="160" width="675" height="68" fill="var(--bar-light)"/>
    <rect x="0" y="226" width="675" height="3" fill="var(--band-blue)"/>
    <!-- content body -->
    <rect x="0" y="229" width="675" height="349" fill="var(--deep-blue)"/>
    <!-- preferences band -->
    <rect x="0" y="578" width="675" height="59" fill="var(--band-blue)"/>
    <!-- preferences body -->
    <rect x="0" y="637" width="675" height="365" fill="var(--deep-blue)"/>
    <!-- bottom nav -->
    <path d="M0 1002 L675 1002 L675 1130 L450 1130 L425 1163 L250 1163 L225 1130 L0 1130 Z" fill="var(--band-blue)"/>
    <path d="M225 1002 L450 1002 L450 1130 L425 1163 L250 1163 L225 1130 Z" fill="var(--panel-blue)"/>
    <path d="M0 1002 L675 1002" stroke="var(--edge-blue)" stroke-width="2"/>
  </svg>

  <h1 class="section-title profile-title">USER PROFILE</h1>

  <section class="profile-card">
    <div class="avatar" role="img" aria-label="User profile photo">
      <svg class="avatar-camera" width="40" height="32" viewBox="0 0 40 32" aria-hidden="true">
        <path d="M4 8 H12 L15 4 H25 L28 8 H36 V28 H4 Z" fill="none" stroke="var(--white)" stroke-width="2.5"/>
        <circle cx="20" cy="17" r="6" fill="none" stroke="var(--white)" stroke-width="2.5"/>
      </svg>
    </div>
    <p class="profile-name">Kolade</p>
    <p class="profile-age">36</p>
  </section>

  <h2 class="section-title preferences-title">PREFERENCES</h2>

  <section class="preferences">
    <p class="pref-label">Distance</p>
    <div class="distance-slider" role="slider" aria-label="Distance" aria-valuenow="48">
      <div class="slider-track"></div>
      <div class="slider-fill"></div>
      <div class="slider-thumb"></div>
    </div>
  </section>

  <nav class="bottom-nav">
    <svg class="nav-item nav-profile" width="52" height="62" viewBox="0 0 52 62" aria-label="Profile">
      <circle cx="26" cy="15" r="14" fill="var(--accent)"/>
      <path d="M2 60 C2 40 12 33 26 33 C40 33 50 40 50 60 Z" fill="var(--accent)"/>
    </svg>
    <svg class="nav-item nav-training" width="150" height="80" viewBox="0 0 150 80" aria-label="Training">
      <g fill="none" stroke="var(--icon-blue)" stroke-width="6" stroke-linecap="round" stroke-linejoin="round">
        <path d="M10 22 H34"/>
        <path d="M4 36 H26"/>
        <path d="M40 74 L56 52 L70 58 L82 34 L98 44"/>
        <path d="M58 52 L74 26 L94 30"/>
        <path d="M74 26 L60 38"/>
        <path d="M88 72 L104 52 L118 58 L128 38 L144 46"/>
      </g>
      <circle cx="90" cy="14" r="8" fill="var(--icon-blue)"/>
      <circle cx="134" cy="24" r="7" fill="var(--icon-blue)"/>
    </svg>
    <svg class="nav-item nav-group" width="72" height="56" viewBox="0 0 72 56" aria-label="Groups">
      <circle cx="14" cy="12" r="8" fill="var(--icon-blue)"/>
      <circle cx="58" cy="12" r="8" fill="var(--icon-blue)"/>
      <path d="M0 40 C0 28 6 23 14 23 C20 23 24 26 26 30 L22 40 Z" fill="var(--icon-blue)"/>
      <path d="M72 40 C72 28 66 23 58 23 C52 23 48 26 46 30 L50 40 Z" fill="var(--icon-blue)"/>
      <circle cx="36" cy="20" r="10" fill="var(--icon-blue)"/>
      <path d="M16 56 C16 40 24 33 36 33 C48 33 56 40 56 56 Z" fill="var(--icon-blue)"/>
    </svg>
  </nav>
</main>
</body>
</html>
```